Flyer for an IT consultancy firm

We are an IT consultancy firm based in Iceland. We have a website at: www.brimvolt.com where you can get acquainted with our activities.
We require a double-sided flyer in A4 format to be handed out in conferences, trade shows etc. The flyer is basically a summarized overview of our range of services.

The deliverable should incorporate some visual elements that are relevant to our line of business such as:
• computers
• cybersecurity
• networks
Also, it would be nice to have visuals relating to Icelandic geography, to further emphasize our local roots. Some suggested keywords:
• volcano
• aurora borealis
• waterfall
• glacier

NB: the flyer will be printed out, therefore image resolution needs to be high enough to render nicely on paper.
The primary colors would be red, black and white – in line with our logo. But there is freedom to diverge and go for a different color scheme.

The logo should be present on the top front of the flyer. The URL www.brimvolt.com needs to be mentioned prominently, for example at the bottom of the page.

Examples of design we like:
• https://www.pixelbazaar.net/design/24252027
• https://www.pixelbazaar.net/design/24291120

Attached:
• the text for the brochure in PDF format
• our logo in vector format

IT, software, cybersecurity

EB3D1F
EC4F4E
F09395
F8D3D4
FCEDEE

• existing logo, and visuals related to computer, networks etc
• Icelandic geography/landscapes

```html
<!DOCTYPE html>
<html lang="en">
<head>
<meta charset="utf-8">
<title>Brimvolt – IT Services Flyer</title>
<link rel="stylesheet" href="https://fonts.googleapis.com/css2?family=Exo+2:wght@700;800&family=Poppins:wght@400;500;600;700&family=Oswald:wght@600&display=swap">
<style>
  :root{
    --red:#b3141f;
    --red-deep:#8c0f18;
    --red-bright:#eb3d1f;
    --red-soft:#ec4f4e;
    --black:#0c0c0d;
    --ink:#1d1d1f;
    --white:#ffffff;
    --stage:#9a9a9a;
    --font-head:"Exo 2", sans-serif;
    --font-body:"Poppins", sans-serif;
    --font-phone:"Oswald", sans-serif;
  }
  *{box-sizing:border-box;margin:0;padding:0}
  html,body{width:857px;height:1200px;overflow:hidden;background:var(--stage)}
  .canvas{position:relative;width:857px;height:1200px;overflow:hidden;background:var(--stage);font-family:var(--font-body)}
  .page{position:absolute;top:317px;width:400px;height:566px;background:var(--white);overflow:hidden;box-shadow:0 6px 18px rgba(0,0,0,.35)}
  .page--front{left:20px}
  .page--back{left:437px}
  .page__art{position:absolute;inset:0;width:400px;height:566px}
  .abs{position:absolute}

  /* front */
  .brand{position:absolute;left:66px;top:22px;display:flex;align-items:center;gap:14px}
  .brand__dot{width:58px;height:58px;border-radius:50%;border:5px solid var(--red)}
  .brand__name{font-family:var(--font-head);font-weight:800;font-size:34px;color:var(--ink);letter-spacing:1px}
  .corner{position:absolute;right:13px;top:12px;width:38px;height:28px;border-top:2px solid var(--ink);border-right:2px solid var(--ink)}
  .headline{position:absolute;left:0;width:400px;top:132px;text-align:center;font-family:var(--font-head);font-weight:800;font-size:26px;line-height:1.02;color:var(--white)}
  .intro{position:absolute;left:44px;top:191px;width:330px;font-size:7.3px;line-height:1.24;color:var(--white);white-space:nowrap}

  .service__icon{position:absolute;width:34px;height:38px}
  .service__title{position:absolute;font-weight:700;font-size:9px;line-height:1.15;letter-spacing:.2px;text-transform:uppercase}
  .service__title::after{content:"";display:block;width:34px;height:2px;background:var(--red);margin-top:4px}
  .service__text{position:absolute;font-size:6.4px;line-height:1.3}
  .service__tag{position:absolute;font-size:6.4px;line-height:1.3}
  .divider{position:absolute;left:196px;top:404px;width:1px;height:124px;background:#bbb}
  .front-url{position:absolute;left:0;width:400px;top:540px;text-align:center;font-weight:700;font-size:12.5px;color:var(--white)}

  /* back */
  .dark{color:var(--white)}
  .light{color:var(--ink)}
  .light .service__title,.service__title.light{color:var(--red)}
  .contact-line{position:absolute;left:0;width:400px;top:491px;text-align:center;font-size:7.4px;color:var(--white)}
  .phone-icon{position:absolute;left:22px;top:510px;width:29px;height:29px;border-radius:50%;background:var(--red-bright)}
  .phone-number{position:absolute;left:57px;top:505px;font-family:var(--font-phone);font-weight:600;font-size:30px;line-height:1.1;color:var(--white);letter-spacing:-.5px}
  .web-list{position:absolute;left:263px;top:526px;list-style:none}
  .web-list li{display:flex;align-items:center;gap:4px;font-weight:700;font-size:9px;line-height:1.45;color:var(--white)}
  .web-list li::before{content:"";width:7px;height:7px;border-radius:50%;background:var(--white)}
</style>
</head>
<body>
<main class="canvas">

  <!-- FRONT SIDE -->
  <section class="page page--front">
    <svg class="page__art" viewBox="0 0 400 566" aria-hidden="true">
      <defs>
        <linearGradient id="bandRed" x1="0" y1="0" x2="1" y2="1">
          <stop offset="0" stop-color="#a3121c"/>
          <stop offset="1" stop-color="#7e0c14"/>
        </linearGradient>
      </defs>
      <polygon points="0,134 400,66 400,232 0,298" fill="url(#bandRed)"/>
      <polygon points="0,262 150,270 0,298" fill="#d7191f"/>
      <line x1="0" y1="123" x2="118" y2="104" stroke="#b3141f" stroke-width="1.4"/>
      <circle cx="118" cy="104" r="2.4" fill="#b3141f"/>
      <polyline points="0,536 100,536 112,525 282,525 294,536 400,536" fill="none" stroke="#b3141f" stroke-width="1.6"/>
      <polygon points="0,542 108,542 120,531 280,531 292,542 400,542 400,566 0,566" fill="#0c0c0d"/>
    </svg>
    <svg class="abs" style="left:0;top:228px" width="400" height="164" viewBox="0 0 400 164" role="img" aria-label="Photo: snow-capped Icelandic mountains under green aurora borealis">
      <defs>
        <linearGradient id="auroraPhoto" x1="0" y1="0" x2="0" y2="1">
          <stop offset="0" stop-color="#1f8f96"/>
          <stop offset=".45" stop-color="#5fb2c8"/>
          <stop offset=".75" stop-color="#2f5f86"/>
          <stop offset="1" stop-color="#182a3e"/>
        </linearGradient>
      </defs>
      <polygon points="0,69 400,2 400,164 0,164" fill="url(#auroraPhoto)"/>
    </svg>

    <div class="brand"><span class="brand__dot"></span><span class="brand__name">BRIMVOLT</span></div>
    <div class="corner"></div>

    <h1 class="headline">YOUR ICELANDIC<br>IT PARTNER</h1>
    <p class="intro">Step into a world of comprehensive IT solutions tailored to your unique needs.<br>Our services, available on a contract or as-needed basis, are designed to<br>empower your business and equip you with the tools you need to succeed.<br>More than just a list of offerings, they're a commitment to quality,<br>a dedication to innovation, and a promise<br>of reliability.</p>

    <article class="service light">
      <svg class="service__icon" style="left:29px;top:404px" viewBox="0 0 34 38" aria-hidden="true"><polygon points="17,0 34,9.5 34,28.5 17,38 0,28.5 0,9.5" fill="#b3141f"/><path d="M10 21a5 5 0 0 1 3-9 6 6 0 0 1 11 2 4 4 0 0 1-1 7z" fill="none" stroke="#fff" stroke-width="1.3"/></svg>
      <h2 class="service__title" style="left:70px;top:406px">Software<br>development and<br>integration services</h2>
      <p class="service__text" style="left:29px;top:451px;width:162px">We specialize in custom software development across different platforms (Linux, Windows, embedded systems). We are open source software advocates, and leverage decades of experience to deliver innovative and cost-effective solutions tailored to your needs.</p>
      <p class="service__tag" style="left:29px;top:506px;width:150px">Let's build the perfect software solution for you.</p>
    </article>
    <div class="divider"></div>
    <article class="service light">
      <svg class="service__icon" style="left:210px;top:404px" viewBox="0 0 34 38" aria-hidden="true"><polygon points="17,0 34,9.5 34,28.5 17,38 0,28.5 0,9.5" fill="#b3141f"/><circle cx="17" cy="19" r="7" fill="none" stroke="#fff" stroke-width="1.3"/><circle cx="17" cy="17" r="2.2" fill="#fff"/></svg>
      <h2 class="service__title" style="left:250px;top:410px">Systems<br>administration</h2>
      <p class="service__text" style="left:210px;top:451px;width:164px">Are you having trouble with your IT infrastructure and in need of qualified personnel to take care of them? Or do you simply need a watchful and expert eye to ensure your systems keep running smoothly? We provide on-site and remote sysadmin services to manage your systems and bring you peace of mind.</p>
      <p class="service__tag" style="left:210px;top:514px">Take back control.</p>
    </article>

    <p class="front-url">www.brimvolt.com</p>
  </section>

  <!-- BACK SIDE -->
  <section class="page page--back">
    <svg class="page__art" viewBox="0 0 400 566" aria-hidden="true">
      <polygon points="0,0 200,0 200,290 0,304" fill="#0c0c0d"/>
      <polygon points="200,140 400,118 400,142 200,168" fill="#d9d9d9"/>
      <polygon points="0,483 400,483 400,566 0,566" fill="#0c0c0d"/>
      <polygon points="250,566 262,516 400,510 400,566" fill="#b3141f"/>
      <polyline points="240,566 252,512 400,505" fill="none" stroke="#fff" stroke-width="1.4"/>
      <line x1="205" y1="477" x2="395" y2="466" stroke="#b3141f" stroke-width="1.2"/>
      <circle cx="395" cy="466" r="2.2" fill="#b3141f"/>
    </svg>
    <svg class="abs" style="left:200px;top:0" width="200" height="170" viewBox="0 0 200 170" role="img" aria-label="Photo: blue ice cave inside an Icelandic glacier">
      <defs>
        <linearGradient id="iceCave" x1="0" y1="0" x2="1" y2="1">
          <stop offset="0" stop-color="#0f2f6a"/>
          <stop offset=".5" stop-color="#2a7fd0"/>
          <stop offset="1" stop-color="#0d2b55"/>
        </linearGradient>
      </defs>
      <polygon points="0,0 200,0 200,120 0,166" fill="url(#iceCave)"/>
    </svg>
    <svg class="abs" style="left:0;top:288px" width="200" height="195" viewBox="0 0 200 195" role="img" aria-label="Photo: erupting Icelandic volcano with glowing lava flows">
      <defs>
        <radialGradient id="lava" cx=".55" cy=".35" r=".8">
          <stop offset="0" stop-color="#ff6a1a"/>
          <stop offset=".3" stop-color="#b8320f"/>
          <stop offset=".7" stop-color="#2b1a18"/>
          <stop offset="1" stop-color="#151516"/>
        </radialGradient>
      </defs>
      <polygon points="0,16 200,2 200,195 0,195" fill="url(#lava)"/>
    </svg>

    <article class="service dark">
      <svg class="service__icon" style="left:26px;top:17px" viewBox="0 0 34 38" aria-hidden="true"><polygon points="17,0 34,9.5 34,28.5 17,38 0,28.5 0,9.5" fill="#b3141f"/><rect x="9" y="11" width="16" height="12" fill="none" stroke="#fff" stroke-width="1.3"/><line x1="13" y1="27" x2="21" y2="27" stroke="#fff" stroke-width="1.3"/></svg>
      <h2 class="service__title" style="left:68px;top:24px">Infrastructure<br>monitoring services</h2>
      <p class="service__text" style="left:27px;top:61px;width:166px">Do you know what is really going on inside your systems? We leverage leading open source monitoring solutions to bring visibility to your infrastructure. Monitor your systems proactively to ensure that they remain healthy at all times. Collect logs in real time and be notified when problems occur or warnings are raised.</p>
      <p class="service__tag" style="left:27px;top:123px">Fix issues before they become problems.</p>
    </article>
    <article class="service dark">
      <svg class="service__icon" style="left:26px;top:142px" viewBox="0 0 34 38" aria-hidden="true"><polygon points="17,0 34,9.5 34,28.5 17,38 0,28.5 0,9.5" fill="#b3141f"/><rect x="11" y="10" width="12" height="16" fill="none" stroke="#fff" stroke-width="1.3"/><line x1="14" y1="15" x2="20" y2="15" stroke="#fff"/><line x1="14" y1="19" x2="20" y2="19" stroke="#fff"/></svg>
      <h2 class="service__title" style="left:68px;top:150px">Technology<br>assessment services</h2>
      <p class="service__text" style="left:27px;top:185px;width:166px">Unsure about which tools are right for you or what IT strategy to pursue to help your business grow? We conduct market research and perform technical evaluations of software and hardware products to determine the best solutions for your company.</p>
      <p class="service__tag" style="left:27px;top:232px;width:140px">Let's empower your business with leading-edge solutions.</p>
    </article>
    <article class="service light">
      <svg class="service__icon" style="left:214px;top:176px" viewBox="0 0 34 38" aria-hidden="true"><polygon points="17,0 34,9.5 34,28.5 17,38 0,28.5 0,9.5" fill="#b3141f"/><circle cx="17" cy="19" r="6" fill="none" stroke="#fff" stroke-width="2.2" stroke-dasharray="3 2"/><circle cx="17" cy="19" r="2" fill="#fff"/></svg>
      <h2 class="service__title" style="left:259px;top:189px">Automation</h2>
      <p class="service__text" style="left:216px;top:220px;width:166px">Because you need effective tools to grow and prosper, it is essential that your IT systems align with your operational needs. We offer a comprehensive review of your business and IT environment so as to optimize the means already at your disposal. We streamline your workflow and develop new tools as needed, to make your IT systems work harder for you.</p>
      <p class="service__tag" style="left:216px;top:290px">Let us automate the boring stuff for you.</p>
    </article>
    <article class="service light">
      <svg class="service__icon" style="left:214px;top:309px" viewBox="0 0 34 38" aria-hidden="true"><polygon points="17,0 34,9.5 34,28.5 17,38 0,28.5 0,9.5" fill="#b3141f"/><rect x="12" y="17" width="10" height="9" fill="#fff"/><path d="M14 17v-3a3 3 0 0 1 6 0v3" fill="none" stroke="#fff" stroke-width="1.3"/></svg>
      <h2 class="service__title" style="left:259px;top:322px">Security services</h2>
      <p class="service__text" style="left:216px;top:354px;width:168px">We understand the importance of security in today's digital landscape. That's why we offer comprehensive security services, including network audits to find and remedy flaws before they can be exploited to your disadvantage.</p>
      <p class="service__text" style="left:216px;top:399px;width:168px">We perform a thorough review of your IT environment to identify and remediate the weakspots, in order to keep your business secure, protect your assets and your reputation. Let's raise your security posture to the highest standards, so that you don't become the next victim – or headline.</p>
      <p class="service__tag" style="left:216px;top:455px">Bring the good guys in to keep the bad guys out.</p>
    </article>

    <p class="contact-line">Get in touch with us today to discuss your IT needs in strict confidence.</p>
    <span class="phone-icon"></span>
    <p class="phone-number">+354 555 0148</p>
    <ul class="web-list">
      <li>www.brimvolt.com</li>
      <li>www.brimvolt.com</li>
    </ul>
  </section>

</main>
</body>
</html>
```